Equity, Effectiveness and Efficiency in charitable food relief sector

I am undertaking my PhD in food policy in the charitable food relief sector, specifically investigating the factors (supply, demand and capacity) that affect the introduction of nutrition policy and in turn, affect the sector's ability to achieve equity, effectiveness and efficiency.

I need a graphic device that incorporates this central idea of Equity, Effectiveness and Efficiency, and how the factors of supply, demand and capacity interact. There are sub-factors within supply (1-6), demand (7-10) and capacity (11 - 15). All these details are shown in the attached figure (Basic figure_Eq Effec Effic and factors.jpg)

This figure (Basic figure_Eq Effec Effic and factors.jpg) contains all the information I need in a graphic but I need something that is more visually appealing, and that can link the ideas in a format other than a table. The final graphic will outline how the food relief sector balances the core objectives of equity, effectiveness and efficiency with the factors (and sub-factors) of supply, demand and capacity.

```html
<!DOCTYPE html>
<html lang="en">
<head>
<meta charset="utf-8">
<title>Equity, Effectiveness, Efficiency – Factors affecting nutrition policy</title>
<link rel="stylesheet" href="https://fonts.googleapis.com/css2?family=Oswald:wght@600;700&family=Montserrat:wght@400;700&display=swap">
<style>
  :root {
    --page-bg: #e4e4e4;
    --navy-deep: #04183a;
    --navy-bright: #0a58bd;
    --title-gold: #ffab00;
    --sidebar-blue: #27b6ef;
    --heading-navy: #163b7c;
    --body-ink: #1c1c1c;
    --band-grey: #ebebeb;
    --card-white: #ffffff;
  }
  * { margin: 0; padding: 0; box-sizing: border-box; }
  html, body {
    width: 1200px; height: 947px; overflow: hidden;
    background: var(--page-bg);
  }
  .card {
    position: absolute; left: 20px; top: 63px;
    width: 1160px; height: 820px;
    background: var(--card-white);
    box-shadow: 0 6px 18px rgba(0,0,0,0.25);
    overflow: hidden;
  }
  .header {
    position: absolute; left: 0; top: 0; width: 100%; height: 132px;
    background: linear-gradient(90deg, var(--navy-deep) 0%, #073c8a 30%, var(--navy-bright) 50%, #073c8a 70%, var(--navy-deep) 100%);
    display: flex; align-items: center; justify-content: center;
  }
  .header h1 {
    font-family: "Oswald", "Arial Narrow", sans-serif;
    font-weight: 700; font-size: 76px; line-height: 1;
    color: var(--title-gold); letter-spacing: 0.5px;
    transform: scaleY(1.08);
    text-shadow: 0 2px 3px rgba(0,0,0,0.35);
    padding-top: 4px;
  }
  .sidebar {
    position: absolute; left: 0; top: 132px; width: 176px; height: 688px;
    background: var(--sidebar-blue);
  }
  .sidebar-title {
    position: absolute; left: 88px; top: 344px;
    width: 560px;
    transform: translate(-50%, -50%) rotate(-90deg);
    font-family: "Oswald", "Arial Narrow", sans-serif;
    font-weight: 700; font-size: 46px; line-height: 56px;
    color: #fff; text-align: center; white-space: nowrap;
    letter-spacing: -0.5px;
  }
  .factor-row { position: absolute; left: 0; width: 100%; height: 196px; }
  .factor-row.supply { top: 156px; }
  .factor-row.demand { top: 372px; }
  .factor-row.capacity { top: 588px; }
  .band {
    position: absolute; left: 310px; top: 0; width: 760px; height: 196px;
    background: linear-gradient(90deg, var(--band-grey) 0%, var(--band-grey) 45%, rgba(235,235,235,0) 100%);
  }
  .hex-badge {
    position: absolute; left: 203px; top: -2px; width: 178px; height: 200px;
    filter: drop-shadow(0 2px 4px rgba(0,0,0,0.22));
  }
  .factor-text {
    position: absolute; left: 403px; top: 0;
    font-family: "Montserrat", Arial, sans-serif;
    color: var(--body-ink);
  }
  .factor-text h2 {
    font-weight: 700; font-size: 33px; line-height: 1;
    color: var(--heading-navy); letter-spacing: 0.3px;
  }
  .factor-text p {
    font-weight: 400; font-size: 19.5px; line-height: 30.3px;
    white-space: pre;
  }
  .supply .factor-text h2 { margin-top: 36px; }
  .supply .factor-text p { margin-top: 10px; }
  .demand .factor-text h2 { margin-top: 37px; }
  .demand .factor-text p { margin-top: 23px; }
  .capacity .factor-text h2 { margin-top: 17px; }
  .capacity .factor-text p { margin-top: 5px; }
</style>
</head>
<body>
  <main class="card">
    <header class="header">
      <h1>EQUITY, EFFECTIVENESS, EFFICIENCY</h1>
    </header>

    <aside class="sidebar">
      <div class="sidebar-title">Factors affecting the introduction<br>of nutrition policy</div>
    </aside>

    <section class="factor-row supply">
      <div class="band"></div>
      <svg class="hex-badge" viewBox="0 0 178 200" aria-hidden="false">
        <defs>
          <linearGradient id="ring-supply" x1="0" y1="0" x2="0" y2="1">
            <stop offset="0" stop-color="#fdc02a"/>
            <stop offset="1" stop-color="#f36b2b"/>
          </linearGradient>
        </defs>
        <polygon points="89,0 178,50 178,150 89,200 0,150 0,50" fill="#fff"/>
        <polygon points="89,8 170,54 170,146 89,192 8,146 8,54" fill="url(#ring-supply)"/>
        <polygon points="89,25 155,63 155,137 89,175 23,137 23,63" fill="#fff"/>
        <rect x="49" y="55" width="80" height="90" rx="8" fill="#eef2f8" role="img" aria-label="Supply icon: parcel linked in a network"/>
      </svg>
      <div class="factor-text">
        <h2>SUPPLY</h2>
        <p>1.  Uncertain material supply   2. Uncertain monetary supply
3. Limited food supply   4.  Perishability  5.  Donor constraints
6. Donor relationships</p>
      </div>
    </section>

    <section class="factor-row demand">
      <div class="band"></div>
      <svg class="hex-badge" viewBox="0 0 178 200">
        <defs>
          <linearGradient id="ring-demand" x1="0" y1="0" x2="0" y2="1">
            <stop offset="0" stop-color="#2cc3f5"/>
            <stop offset="1" stop-color="#1a9bd8"/>
          </linearGradient>
        </defs>
        <polygon points="89,0 178,50 178,150 89,200 0,150 0,50" fill="#fff"/>
        <polygon points="89,8 170,54 170,146 89,192 8,146 8,54" fill="url(#ring-demand)"/>
        <polygon points="89,25 155,63 155,137 89,175 23,137 23,63" fill="#fff"/>
        <rect x="49" y="55" width="80" height="90" rx="8" fill="#eef2f8" role="img" aria-label="Demand icon: rising bar chart beside a light bulb with a dollar sign"/>
      </svg>
      <div class="factor-text">
        <h2>DEMAND</h2>
        <p>7. Uncertain demand  8.  Limited demand visibility
9. Client choice   10.  Food wastage</p>
      </div>
    </section>

    <section class="factor-row capacity">
      <div class="band"></div>
      <svg class="hex-badge" viewBox="0 0 178 200">
        <defs>
          <linearGradient id="ring-capacity" x1="0" y1="0" x2="0" y2="1">
            <stop offset="0" stop-color="#13a51e"/>
            <stop offset="1" stop-color="#0b9a17"/>
          </linearGradient>
        </defs>
        <polygon points="89,0 178,50 178,150 89,200 0,150 0,50" fill="#fff"/>
        <polygon points="89,8 170,54 170,146 89,192 8,146 8,54" fill="url(#ring-capacity)"/>
        <polygon points="89,25 155,63 155,137 89,175 23,137 23,63" fill="#fff"/>
        <rect x="49" y="55" width="80" height="90" rx="8" fill="#eef2f8" role="img" aria-label="Capacity icon: stacked boxes in front of a gear"/>
      </svg>
      <div class="factor-text">
        <h2>CAPACITY</h2>
        <p>11. Storage:  a)  Cold   b)  Warehouse  12. Transportation
13. Workforce : a)  Volunteers  b)  Expertise and training
c)  Attitudes and Belief  d)  Collaboration  e) Executive Support
14. External stakeholders  15.  Budget</p>
      </div>
    </section>
  </main>
</body>
</html>
```